Private Ambulance Company

I’m looking for a vehicle design wrap for our ambulance that incorporates our logo and color scheme. I have included a picture of the actual vehicle that needs to be rewrapped. 2021 Oku Stelvane

```html
<!DOCTYPE html>
<html lang="en">
<head>
<meta charset="utf-8">
<title>Summit Carers – Vehicle Wrap Panels</title>
<link rel="stylesheet" href="https://fonts.googleapis.com/css2?family=Montserrat:wght@500;600&family=Oswald:wght@500&family=Poppins:wght@300&display=swap">
<style>
  :root{
    --page:#f3f3f3;
    --panel:#ffffff;
    --sky:#00aeef;
    --sky-soft:#bfe6fb;
    --sky-glow:#5fcaf8;
    --teal:#0f7a78;
    --teal-soft:#3fb4b6;
    --gold:#c9952b;
    --ink:#1e2a30;
    --plus:#7cc46a;
  }
  *{margin:0;padding:0;box-sizing:border-box}
  html,body{width:837px;height:1200px;overflow:hidden;background:var(--page)}
  .sheet{position:relative;width:837px;height:1200px}
  .panel{position:absolute;overflow:hidden;background:var(--panel)}
  .panel--side{left:40px;top:224px;width:757px;height:311px;
    background:
      radial-gradient(ellipse 260px 110px at 360px 330px,var(--sky-glow),transparent 70%),
      radial-gradient(ellipse 300px 160px at 0 0,#dff4fe,transparent 70%),
      var(--panel)}
  .panel--door{left:40px;top:543px;width:436px;height:179px;
    background:
      radial-gradient(ellipse 170px 70px at 190px 190px,var(--sky-glow),transparent 70%),
      radial-gradient(ellipse 160px 90px at 0 0,#dff4fe,transparent 70%),
      var(--panel)}
  .panel--rear{left:484px;top:543px;width:313px;height:330px;
    background:
      radial-gradient(ellipse 200px 120px at 0 0,var(--sky-glow),transparent 75%),
      radial-gradient(ellipse 190px 120px at 313px 330px,var(--sky-glow),transparent 75%),
      var(--panel)}
  .panel--hood{left:484px;top:881px;width:313px;height:94px;
    background:
      radial-gradient(ellipse 90px 70px at 0 0,var(--sky-glow),transparent 75%),
      radial-gradient(ellipse 110px 60px at 313px 94px,var(--sky-glow),transparent 75%),
      var(--panel)}

  .check-band{position:absolute;background:var(--sky-soft);opacity:.85}

  .brand{position:absolute;display:flex;flex-direction:column}
  .brand__row{display:flex;align-items:center}
  .brand__mark{background:var(--teal);flex:none}
  .brand__name{font-family:"Montserrat",sans-serif;font-weight:600;color:var(--teal);letter-spacing:.08em;white-space:nowrap;line-height:1}
  .brand__tag{font-family:"Montserrat",sans-serif;font-weight:500;color:var(--teal-soft);letter-spacing:.18em;white-space:nowrap}

  .phone{position:absolute;background:var(--sky);color:#fff;font-family:"Oswald",sans-serif;font-weight:500;display:flex;align-items:center;letter-spacing:-.01em;line-height:1}

  .services{position:absolute;font-family:"Poppins",sans-serif;font-weight:300;color:var(--ink)}
  .services__title{font-family:"Oswald",sans-serif;font-weight:500;color:var(--sky);font-size:17px;letter-spacing:-.02em;line-height:1;margin-bottom:7px}
  .services__list{list-style:none;font-size:13px;line-height:20px}
  .services__list li{display:flex;align-items:center;gap:7px}
  .services__list li::before{content:"+";color:var(--plus);font-weight:600;font-size:11px}

  .unit-tag{position:absolute;background:var(--sky);color:#fff;font-family:"Poppins",sans-serif;font-weight:300;display:flex;align-items:center;justify-content:center;line-height:1}
</style>
</head>
<body>
<main class="sheet">

  <section class="panel panel--side" aria-label="Side wrap panel">
    <div class="check-band" role="img" aria-label="Checkered light-blue band" style="left:0;top:34px;width:502px;height:18px"></div>
    <div class="brand" style="left:43px;top:80px">
      <div class="brand__row" style="gap:10px">
        <span class="brand__mark" style="width:34px;height:34px"></span>
        <span class="brand__name" style="font-size:27px">SUMMIT CARERS</span>
      </div>
      <span class="brand__tag" style="font-size:10px;margin:9px 0 0 44px">Your Health, Our Priority</span>
    </div>
    <div class="phone" style="left:0;top:168px;width:283px;height:60px;font-size:46px;justify-content:flex-end;padding-right:13px">123-456-789</div>
    <div class="services" style="left:297px;top:172px">
      <h2 class="services__title">OUR SERVICES</h2>
      <ul class="services__list">
        <li>Hospital Discharges</li>
        <li>Clinical Appointments</li>
      </ul>
    </div>
    <div class="unit-tag" style="left:514px;top:215px;width:36px;height:14px;font-size:8px">Unit 04</div>
  </section>

  <section class="panel panel--door" aria-label="Rear door wrap panel">
    <div class="check-band" role="img" aria-label="Checkered light-blue band" style="left:0;top:18px;width:289px;height:11px"></div>
    <div class="brand" style="left:73px;top:44px">
      <div class="brand__row" style="gap:6px">
        <span class="brand__mark" style="width:20px;height:20px"></span>
        <span class="brand__name" style="font-size:16px">SUMMIT CARERS</span>
      </div>
      <span class="brand__tag" style="font-size:6px;margin:6px 0 0 26px">Your Health, Our Priority</span>
    </div>
    <div class="phone" style="left:73px;top:95px;width:146px;height:37px;font-size:29px;justify-content:center">123-456-789</div>
    <div class="unit-tag" style="left:298px;top:123px;width:20px;height:7px;font-size:4.5px">Unit 04</div>
  </section>

  <section class="panel panel--rear" aria-label="Rear wrap panel">
    <div class="check-band" role="img" aria-label="Checkered light-blue band" style="left:158px;top:24px;width:155px;height:17px"></div>
    <div class="brand" style="left:53px;top:100px">
      <div class="brand__row" style="gap:8px">
        <span class="brand__mark" style="width:26px;height:26px"></span>
        <span class="brand__name" style="font-size:20px">SUMMIT CARERS</span>
      </div>
      <span class="brand__tag" style="font-size:8px;margin:8px 0 0 34px">Your Health, Our Priority</span>
    </div>
    <div class="phone" style="left:0;top:159px;width:313px;height:43px;font-size:36px;padding-left:70px">123-456-789</div>
    <div class="check-band" role="img" aria-label="Checkered light-blue band" style="left:0;top:253px;width:157px;height:17px"></div>
  </section>

  <section class="panel panel--hood" aria-label="Bonnet wrap panel">
    <div class="brand" style="left:76px;top:27px">
      <div class="brand__row" style="gap:7px">
        <span class="brand__mark" style="width:22px;height:22px"></span>
        <span class="brand__name" style="font-size:17px">SUMMIT CARERS</span>
      </div>
      <span class="brand__tag" style="font-size:7px;margin:7px 0 0 29px">Your Health, Our Priority</span>
    </div>
  </section>

</main>
</body>
</html>
```